Images and design ideas provided: Postcard size flier

2 sided postcard size flier to hand people on the street.

A FUN tax business needs a postcard size flier to hand people on the street. Not a typical serious, quiet, office so make the image fun!

Exact wording, logo and key images provided. You are free to add other images as you see fit (such as money).

Side 1: Use image of lady looking up (she should be looking at text provided).All spanish and english text provided. Logo in bottom right corner. Address at bottom of card.

Side 2: Image of lady holding money and pointing. Remove money and have her holding a sign/or some other creative way to have her looking at text. All spanish and english text provided. Logo in bottom right corner. Address at bottom of card.

Size: 4" x 6" horizontal or vertical is ok
Each side can be different and image/design does not have to be related.

Target Market(s)

Age 18-35

Industry/Entity Type

Accounting

Font styles to use
Sans Serif

Colors

Designer to choose colors to be used in the design.

Requirements
Must have
• Use text document provided. All text goes on both sides.
• Should be easy to read from a few feet away.
Nice to have
• Bright colors to attract attention of people walking by to grab flier/card. Images of money ok.
Should not have
• No images of calculators or typical accounting tax forms.

```html
<!DOCTYPE html>
<html lang="en">
<head>
<meta charset="utf-8">
<title>Brightside Returns – Postcard Flier</title>
<link href="https://fonts.googleapis.com/css2?family=Exo+2:wght@500;600;700;800&display=swap" rel="stylesheet">
<style>
  :root {
    --backdrop: #6f6f6f;
    --card-white: #f7f7f7;
    --band-white: rgba(255,255,255,0.82);
    --money-light: #e4e6e4;
    --money-mid: #c9cec9;
    --money-green: #b9c4ba;
    --brand-blue: #2f6db3;
    --brand-red: #e0213f;
    --robe-gold: #9a9a5a;
    --robe-red: #b52a2a;
    --cloud: #ffffff;
  }
  * { margin: 0; padding: 0; box-sizing: border-box; }
  html, body { width: 1200px; height: 1000px; overflow: hidden; }
  body {
    background: radial-gradient(ellipse at center, #7a7a7a 0%, var(--backdrop) 100%);
    font-family: "Exo 2", sans-serif;
    position: relative;
  }
  .flier {
    position: absolute;
    width: 513px;
    height: 770px;
    background: var(--card-white);
    overflow: hidden;
    box-shadow: 0 4px 10px rgba(0,0,0,0.35);
  }
  .flier--front { left: 65px; top: 108px; }
  .flier--back { left: 633px; top: 110px; }

  .money-backdrop {
    position: absolute; inset: 0;
    background:
      linear-gradient(160deg, var(--money-light) 0%, var(--money-mid) 45%, var(--money-green) 70%, var(--money-light) 100%);
  }
  .logo-band {
    position: absolute; left: 0; top: 0; width: 100%; height: 118px;
    background: var(--band-white);
    display: flex; align-items: center; justify-content: center; gap: 14px;
  }
  .logo-band__dot {
    width: 30px; height: 30px; border-radius: 50%; background: var(--brand-blue);
  }
  .logo-band__name {
    font-weight: 600; font-size: 38px; line-height: 1; color: var(--brand-blue);
  }

  .cloud { position: absolute; filter: drop-shadow(0 3px 4px rgba(0,0,0,0.25)); }
  .cloud svg { position: absolute; inset: 0; width: 100%; height: 100%; }
  .cloud__text {
    position: absolute; inset: 0;
    display: flex; flex-direction: column; align-items: center; justify-content: center;
    color: var(--brand-blue); font-weight: 600; text-align: center;
  }
  .offer-cloud { left: 148px; top: 128px; width: 356px; height: 240px; }
  .offer-cloud .cloud__text { padding-top: 8px; }
  .offer-cloud__lead { font-size: 38px; line-height: 1.15; }
  .offer-cloud__amount { font-size: 52px; font-weight: 800; color: var(--brand-red); line-height: 1.15; }
  .offer-cloud__tail { font-size: 38px; line-height: 1.15; }
  .note-cloud { left: 372px; top: 360px; width: 138px; height: 92px; }
  .note-cloud .cloud__text { font-size: 15px; line-height: 1.25; padding-top: 6px; }

  .contact-cloud { left: 108px; top: 10px; width: 292px; height: 172px; }
  .contact-cloud .cloud__text { font-size: 44px; line-height: 1.12; padding-top: 10px; }

  .contact-band {
    position: absolute; left: 0; top: 210px; width: 100%; height: 126px;
    background: rgba(255,255,255,0.7);
    display: flex; flex-direction: column; align-items: center; justify-content: center;
    color: var(--brand-blue); font-weight: 600; font-size: 26px; line-height: 1.25;
  }

  .model-photo {
    position: absolute;
    background: linear-gradient(180deg, var(--robe-red) 0%, var(--robe-gold) 35%, #8c8a5c 100%);
  }
  .flier--front .model-photo { left: 20px; top: 362px; width: 355px; height: 370px; border-radius: 140px 140px 0 0; }
  .flier--back .model-photo { left: 128px; top: 360px; width: 250px; height: 370px; border-radius: 110px 110px 0 0; }

  .url-band {
    position: absolute; left: 0; bottom: 0; width: 100%; height: 42px;
    background: var(--band-white);
    display: flex; align-items: center; justify-content: center;
    color: var(--brand-red); font-weight: 700; font-size: 21px; letter-spacing: 0.3px;
  }
</style>
</head>
<body>

<section class="flier flier--front">
  <div class="money-backdrop" role="img" aria-label="Stack of hundred-dollar bills, softly faded"></div>
  <header class="logo-band">
    <span class="logo-band__dot"></span>
    <span class="logo-band__name">Brightside Returns</span>
  </header>

  <div class="cloud offer-cloud">
    <svg viewBox="0 0 356 240" aria-hidden="true">
      <g fill="var(--cloud)">
        <circle cx="80" cy="150" r="70"/>
        <circle cx="160" cy="95" r="88"/>
        <circle cx="250" cy="110" r="72"/>
        <circle cx="290" cy="160" r="60"/>
        <ellipse cx="180" cy="175" rx="150" ry="62"/>
      </g>
    </svg>
    <div class="cloud__text">
      <span class="offer-cloud__lead">Get</span>
      <span class="offer-cloud__amount">$100</span>
      <span class="offer-cloud__tail">Cash Now!</span>
    </div>
  </div>

  <div class="cloud note-cloud">
    <svg viewBox="0 0 138 92" aria-hidden="true">
      <g fill="var(--cloud)">
        <circle cx="40" cy="55" r="30"/>
        <circle cx="70" cy="38" r="34"/>
        <circle cx="102" cy="52" r="30"/>
        <ellipse cx="69" cy="64" rx="62" ry="26"/>
      </g>
    </svg>
    <div class="cloud__text">with paid<br>tax preparation</div>
  </div>

  <div class="model-photo" role="img" aria-label="Smiling woman in a costume robe and tall hat, arms raised, looking up at the offer"></div>
  <footer class="url-band">WWW.BRIGHTSIDERETURNS.COM</footer>
</section>

<section class="flier flier--back">
  <div class="money-backdrop" role="img" aria-label="Scattered hundred-dollar bills, softly faded"></div>

  <div class="cloud contact-cloud">
    <svg viewBox="0 0 292 172" aria-hidden="true">
      <g fill="var(--cloud)">
        <circle cx="60" cy="100" r="50"/>
        <circle cx="130" cy="68" r="64"/>
        <circle cx="210" cy="78" r="54"/>
        <circle cx="245" cy="115" r="42"/>
        <ellipse cx="150" cy="125" rx="125" ry="44"/>
      </g>
    </svg>
    <div class="cloud__text">Contact<br>Us</div>
  </div>

  <div class="contact-band">
    <span>(555) 014-2270</span>
    <span>418 Maple Ave. Riverton</span>
    <span>NY 10999</span>
  </div>

  <div class="model-photo" role="img" aria-label="Smiling woman in a costume robe and tall hat holding out a fan of cash"></div>
  <footer class="url-band">WWW.BRIGHTSIDERETURNS.COM</footer>
</section>

</body>
</html>
```